Letterhead Design Project

I need a letterhead design that uses the same design ideas as my business card, which I have attached. I need it to look professional but also fresh and clean. If possible I would also like a with compliments slip and envelope designed as well.

I have attached a copy of a sample word doc for the letterhead that shows everything that must be on it. I would also like an alternative with all of the information in the header. The with compliments slip must also have the same information on it.
With regards to the envelope I only really need the logo and my po box address.

Target Market(s)

30+ Professionals

Industry/Entity Type

Business

Requirements
Must have
• I have attached a copy of a sample word doc for the letterhead that shows everything that must be on it. I would also like an alternative with all of the information in the header. The with compliments slip must also have the same information on it.
Should not have
• I am not looking for anything with traditional text as I can do that myself. I am looking for something that will stand out from the crowd.

```html
<!DOCTYPE html>
<html lang="en">
<head>
<meta charset="utf-8">
<title>Calder Insurance Letterhead</title>
<link rel="stylesheet" href="https://fonts.googleapis.com/css2?family=Questrial&display=swap">
<style>
  :root {
    --charcoal: #333335;
    --charcoal-light: #4a4a4c;
    --signal-red: #e4172f;
    --paper: #ffffff;
    --ink-light: #f2f2f2;
    --ink-muted: #bdbdbd;
  }
  html, body {
    margin: 0;
    padding: 0;
    overflow: hidden;
    background: var(--paper);
  }
  .letterhead {
    position: relative;
    width: 925px;
    height: 1200px;
    overflow: hidden;
    font-family: "Questrial", sans-serif;
    color: var(--ink-light);
  }
  .letterhead__shapes {
    position: absolute;
    inset: 0;
  }
  .brand {
    position: absolute;
    left: 62px;
    top: 26px;
    width: 330px;
  }
  .brand__name {
    font-size: 34px;
    line-height: 1;
    color: var(--ink-light);
    letter-spacing: 0.5px;
    white-space: nowrap;
  }
  .brand__tagline {
    margin-top: 9px;
    padding-left: 2px;
    font-size: 11px;
    letter-spacing: 2.4px;
    color: var(--ink-muted);
    white-space: nowrap;
  }
  .office-address,
  .contact-details {
    position: absolute;
    top: 30px;
    font-style: normal;
    font-size: 13px;
    line-height: 17px;
    color: var(--ink-light);
    white-space: nowrap;
  }
  .office-address { left: 438px; }
  .contact-details { left: 670px; }
  .company-legal {
    position: absolute;
    left: 45px;
    top: 1148px;
    font-size: 15px;
    line-height: 25px;
    color: var(--ink-light);
    white-space: nowrap;
  }
</style>
</head>
<body>
<main class="letterhead">
  <svg class="letterhead__shapes" width="925" height="1200" viewBox="0 0 925 1200" aria-hidden="true">
    <defs>
      <linearGradient id="charcoal-fill" x1="0" y1="0" x2="0" y2="1">
        <stop offset="0" stop-color="var(--charcoal-light)"/>
        <stop offset="1" stop-color="var(--charcoal)"/>
      </linearGradient>
    </defs>
    <rect class="backdrop" width="925" height="1200" fill="url(#charcoal-fill)"/>
    <path class="accent-top" fill="var(--signal-red)"
          d="M560,116 C760,110 915,235 925,370 L925,480 C905,280 760,123 600,123 Z"/>
    <path class="accent-bottom" fill="var(--signal-red)"
          d="M0,1082 C30,1110 70,1124 110,1125 L40,1138 C20,1132 8,1126 0,1120 Z"/>
    <path class="writing-area" fill="var(--paper)"
          d="M0,168 Q0,123 45,123 L600,123 C760,123 905,280 925,470 L925,1060 Q925,1122 862,1125 L110,1125 C70,1124 30,1110 0,1082 Z"/>
  </svg>

  <header>
    <div class="brand">
      <div class="brand__name">Calder Insurance</div>
      <div class="brand__tagline">cover you can count on</div>
    </div>
    <address class="office-address">
      Level 2, 48 Marlowe Street<br>
      Norwood&nbsp; SA&nbsp; 5067<br>
      PO Box 812, Kent Town&nbsp; SA&nbsp; 5071
    </address>
    <address class="contact-details">
      T: 0400 555 318<br>
      F: 08 8000 4127<br>
      E: sam@calderinsurance.com.au<br>
      &nbsp;&nbsp;&nbsp;www.calderinsurance.com.au
    </address>
  </header>

  <footer class="company-legal">
    Calder Insurance Services Pty Ltd&nbsp;&nbsp; ABN 12 345 678 901&nbsp;&nbsp; AR No 500123 as Authorised Representative of<br>
    Harrow Insurance Group Pty Ltd ACN 222 333 444 ABN 55 222 333 444 AFS Licence No 987654
  </footer>
</main>
</body>
</html>
```